Business cards in digital learning for freelancer

Hello, I need a business cards in french. I work in the Digital learning industries as freeelancer; I'm an expert in digital learning. I work in France. My customer are in the health industry, pharmaceutical industry, and training organization. I've got a logo. I offer three services: consulting, Design, and Training. In the consulting, I offers coaching to choose your digital learning tools and the digital learning strategy. For the Design, I product differents level of elearning like rapid-learning, elearning, micro-learning, video-learning. And for the training service, I've create training about pedagogy, digital learning management project, Digital learning design.
I join my Logo create in this platform. My universe is gamified. I like the life, and I'm very social. I want a card like I'm I. I love Art (painting), Europeen comics. I use in my visual support "permanent maker" font and caracters. I would like cards: elegant, modern, Top class. If you need any information, you can ask me.
thanks for ideas

Target Market(s)

in health industries and training organization for Training manager, instructor, human resources director

Contact Information for Business Card

Phone number : 06 31 87 59 14 , mail: lucienmervaux@postelia.fr, web: lucienmervaux.fr , LinkedIn

Font styles to use
Sans Serif

Requirements
Must have
• Use my logo and write my 3 services (consulting, training, design)

```html
<!DOCTYPE html>
<html lang="fr">
<head>
<meta charset="utf-8">
<title>Mervaux Digital Learning – Cartes de visite</title>
<link rel="stylesheet" href="https://fonts.googleapis.com/css2?family=Arimo:wght@400;700&display=swap">
<style>
  :root {
    --orange: #f07224;
    --white: #ffffff;
    --ink: #4a4a4a;
    --rule: #8a8a8a;
    --backdrop: #3b3b3b;
  }
  * { box-sizing: border-box; margin: 0; padding: 0; }
  html, body { width: 1200px; height: 900px; overflow: hidden; }
  body {
    background: var(--backdrop);
    font-family: "Arimo", Arial, sans-serif;
    position: relative;
  }
  .card {
    position: absolute;
    left: 240px;
    width: 720px;
    height: 411px;
    box-shadow: 0 10px 30px rgba(0,0,0,.45);
  }
  .card--front { top: 30px; background: var(--orange); color: var(--white); }
  .card--back  { top: 459px; background: var(--white); color: var(--ink); }

  /* brand lockup */
  .brand { display: flex; align-items: center; gap: 14px; }
  .brand__dot { width: 74px; height: 74px; border-radius: 50%; flex: none; }
  .brand__name { font-weight: 700; letter-spacing: 2px; line-height: 1; }
  .brand__tag { font-weight: 700; letter-spacing: 3px; margin-top: 6px; }

  .card--front .brand {
    position: absolute; left: 50%; top: 110px; transform: translateX(-50%);
  }
  .card--front .brand__dot { background: var(--white); }
  .card--front .brand__name { font-size: 46px; }
  .card--front .brand__tag { font-size: 14px; }

  .services {
    position: absolute; left: 0; right: 0; top: 280px;
    display: flex; justify-content: center; gap: 44px;
    list-style: none; font-size: 22px; letter-spacing: 3px;
  }
  .services li::before {
    content: ""; display: inline-block; width: 8px; height: 8px;
    border-radius: 50%; background: var(--white);
    margin-right: 8px; vertical-align: middle;
  }

  .card--back .brand { position: absolute; right: 50px; top: 48px; color: var(--orange); }
  .card--back .brand__dot { width: 56px; height: 56px; background: var(--orange); }
  .card--back .brand__name { font-size: 34px; }
  .card--back .brand__tag { font-size: 11px; }

  .divider {
    position: absolute; left: 170px; right: 40px; top: 196px;
    height: 1px; background: var(--rule);
  }
  .person { position: absolute; left: 60px; top: 220px; }
  .person__name { color: var(--orange); font-weight: 700; font-size: 30px; letter-spacing: 1px; }
  .person__role { font-size: 21px; margin-top: 4px; }
  .person__rule { width: 230px; height: 1px; background: var(--rule); margin: 16px 0 14px; }

  .contact { list-style: none; font-size: 19px; }
  .contact li { display: flex; align-items: center; gap: 10px; margin-bottom: 8px; }
  .contact svg { width: 16px; height: 16px; fill: var(--orange); flex: none; }

  .online { position: absolute; right: 40px; top: 120px; text-align: right; }
  .online li { justify-content: flex-end; }
  .online .social-dot { width: 14px; height: 14px; border-radius: 50%; background: var(--orange); flex: none; }
</style>
</head>
<body>

<section class="card card--front" aria-label="Recto">
  <div class="brand">
    <span class="brand__dot"></span>
    <div>
      <div class="brand__name">MERVAUX</div>
      <div class="brand__tag">DIGITAL LEARNING</div>
    </div>
  </div>
  <ul class="services">
    <li>Consulting</li>
    <li>Training</li>
    <li>Design</li>
  </ul>
</section>

<section class="card card--back" aria-label="Verso">
  <div class="brand">
    <span class="brand__dot"></span>
    <div>
      <div class="brand__name">MERVAUX</div>
      <div class="brand__tag">DIGITAL LEARNING</div>
    </div>
  </div>

  <ul class="contact online">
    <li>www.lucienmervaux.fr
      <svg viewBox="0 0 16 16" aria-hidden="true"><circle cx="8" cy="8" r="7" fill="none" stroke="#f07224" stroke-width="1.6"/><path d="M1 8h14M8 1c3 3 3 11 0 14M8 1c-3 3-3 11 0 14" fill="none" stroke="#f07224" stroke-width="1.2"/></svg>
    </li>
    <li>@lucienmervaux <span class="social-dot"></span></li>
  </ul>

  <div class="divider"></div>

  <div class="person">
    <div class="person__name">LUCIEN MERVAUX</div>
    <div class="person__role">Creative Director</div>
    <div class="person__rule"></div>
    <ul class="contact">
      <li>
        <svg viewBox="0 0 16 16" aria-hidden="true"><path d="M3.5 1l3 3-1.6 2a9 9 0 0 0 5.1 5.1l2-1.6 3 3-2 2.5C7 14.5 1.5 9 1 3z"/></svg>
        06 31 87 59 14
      </li>
      <li>
        <svg viewBox="0 0 16 16" aria-hidden="true"><path d="M1 3h14v10H1z"/><path d="M1 3l7 6 7-6" fill="none" stroke="#fff" stroke-width="1.4"/></svg>
        lucienmervaux@postelia.fr
      </li>
    </ul>
  </div>
</section>

</body>
</html>
```